Valdorick Business Card Design

Valdorick is the holdings company for my portfolio of businesses. These businesses currently only include Valdorick Advising. V|A is a strategic consulting firm that focuses on small businesses and start-ups that want help with their brand. We focus on partnering with influencers (Pro Athletes and Celebrities) and Social Media Marketing. We also want to focus on companies that have a positive effect on the community or world. The audience I am going after is very corporate. I want to have the corporate edge with some 25yr old flair.
Industry/Entity Type
Business
Contact Information for Business Card
General Idea AttachedLogo (Attached)Jonathan R. MasonCEO & Managing MemberDown Left Bottom CornerPhone: 347-570-0585Cell: 240-604-7930mason@valdorick-example.comDown Right Bottom Corner 174 W 4th St, Ste 212New York, NY 10014www.valdorick-example.comBackside LogoI want the entire card extra thick and with metallic finish
Look and feel

```html
<!DOCTYPE html>
<html lang="en">
<head>
<meta charset="utf-8">
<title>Valdorick Holdings – Business Card</title>
<link rel="stylesheet" href="https://fonts.googleapis.com/css2?family=Open+Sans:wght@400;600&display=swap">
<style>
  :root {
    --backdrop: #e4e5e7;
    --card: #fbfbfa;
    --ink: #5a5a5c;
    --ink-soft: #6b6b6d;
    --accent: #b01e2c;
    --rule: #8a8a8c;
    --rule-light: #c4c4c6;
  }
  * { box-sizing: border-box; margin: 0; padding: 0; }
  html, body {
    width: 1200px; height: 800px; overflow: hidden;
    background: var(--backdrop);
    font-family: "Open Sans", Arial, sans-serif;
  }
  .stage {
    width: 1200px; height: 800px;
    display: flex; align-items: center; justify-content: center;
  }
  .business-card {
    position: relative;
    width: 1050px; height: 600px;
    background: var(--card);
    box-shadow: 0 14px 40px rgba(0,0,0,0.18);
    color: var(--ink);
  }
  .brand {
    position: absolute; left: 160px; top: 80px;
    display: flex; align-items: center; gap: 24px;
  }
  .brand-square {
    width: 96px; height: 96px;
    background: var(--accent);
  }
  .brand-name {
    font-size: 38px; font-weight: 600; letter-spacing: 1px;
    color: var(--accent); text-transform: uppercase;
  }
  .identity {
    position: absolute; left: 0; right: 0; top: 222px;
    text-align: center;
  }
  .person-name {
    font-size: 46px; font-weight: 400; line-height: 1.2;
    color: var(--ink); letter-spacing: 0.5px;
  }
  .person-title {
    display: inline-flex; align-items: center; gap: 14px;
    margin-top: 2px;
    font-size: 18px; color: var(--accent);
  }
  .person-title::before, .person-title::after {
    content: ""; width: 110px; border-top: 1px dashed var(--accent);
  }
  .contact {
    position: absolute; font-size: 24px; line-height: 1.45;
    font-style: normal; color: var(--ink-soft);
  }
  .contact-direct { left: 60px; top: 400px; }
  .contact-office { right: 60px; top: 342px; text-align: right; }
  .base-rules {
    position: absolute; left: 0; right: 0; bottom: 56px;
    border-top: 6px solid var(--rule);
  }
  .base-rules::after {
    content: ""; position: absolute; left: 0; right: 0; top: 10px;
    border-top: 2px solid var(--rule-light);
  }
</style>
</head>
<body>
  <main class="stage">
    <section class="business-card">
      <header class="brand">
        <div class="brand-square"></div>
        <div class="brand-name">Valdorick Holdings LLC</div>
      </header>

      <div class="identity">
        <h1 class="person-name">Derrick L. Fanshaw</h1>
        <p class="person-title">CEO &amp; Managing Member</p>
      </div>

      <address class="contact contact-office">
        88 E 9th St, Ste 405<br>
        New York, NY 10099<br>
        www.valdorick-example.com
      </address>

      <address class="contact contact-direct">
        347-555-0162<br>
        240-555-0187<br>
        fanshaw@valdorick-example.com
      </address>

      <div class="base-rules"></div>
    </section>
  </main>
</body>
</html>
```